Fast Growing Personal Injury Law Firm Needs Business Card Design

We need a business card design for a fast growing personal injury law firm in Florida. Our name is Dorian Halvorsk, P.A. Our practice is comprised of younger attorneys (in their 30s) that employ more modern techniques/tools than our older competition. We would prefer a look that is a modern play on a classic look. Also, we would like to continue using a color scheme that employs navy blue and kelly green (other shades of green could be fine too) as well as our "E" logo.

Industry/Entity Type

Law Firm

```html
<!DOCTYPE html>
<html lang="en">
<head>
<meta charset="utf-8">
<title>Halvorsk Law – Stationery Set</title>
<link rel="stylesheet" href="https://fonts.googleapis.com/css2?family=Open+Sans:wght@400;600&display=swap">
<style>
  :root {
    --green: #0f8a4c;
    --navy: #1f3461;
    --paper: #ffffff;
    --panel: #f3f4f6;
    --board: #5b5b5b;
    --ink: #3a3a3a;
    --accent-red: #d9322c;
    --die: #e6a9b8;
  }
  * { box-sizing: border-box; margin: 0; padding: 0; }
  html, body { width: 1200px; height: 525px; overflow: hidden; background: var(--board); }
  body { font-family: "Open Sans", Arial, sans-serif; color: var(--ink); position: relative; }
  .sheet { position: absolute; background: var(--paper); }
  .panel { position: absolute; background: var(--panel); }
  .abs { position: absolute; }

  /* brand mark: name with a plain square */
  .brand { position: absolute; display: flex; flex-direction: column; align-items: center; justify-content: center; gap: 2px; }
  .brand__square { background: var(--green); border: 1px solid var(--navy); }
  .brand__name { color: var(--navy); font-weight: 600; line-height: 1; white-space: nowrap; }
  .brand--light .brand__square { background: var(--navy); border-color: #fff; }
  .brand--light .brand__name { color: #fff; }

  .band { position: absolute; background: var(--green); }
  .band__block { position: absolute; top: 0; height: 100%; background: var(--navy); }
  .rule { position: absolute; height: 2px; }
  .rule--green { background: var(--green); }
  .rule--navy { background: var(--navy); }

  .contact { position: absolute; line-height: 1.55; white-space: nowrap; color: var(--ink); }
  .contact b { color: var(--accent-red); font-weight: 400; }

  .window { position: absolute; border: 1px solid #c9cdd3; border-radius: 4px; }
  .die { position: absolute; border: 1px solid var(--die); }
</style>
</head>
<body>

<!-- Letterhead -->
<section class="sheet letterhead" style="left:16px;top:15px;width:389px;height:495px;">
  <div class="panel" style="left:9px;top:10px;width:372px;height:477px;"></div>
  <div class="brand" style="left:36px;top:38px;width:48px;height:40px;">
    <span class="brand__square" style="width:24px;height:24px;"></span>
    <span class="brand__name" style="font-size:7px;">Halvorsk</span>
  </div>
  <p class="contact" style="left:226px;top:49px;font-size:4.3px;">2150 Meridian Park Way Suite 410 Palm Harbor Bay, Florida 34299<br><b>P</b> (941) 555-0142 <b>F</b> (941) 555-0187 <b>E</b> dorian@halvorsklaw.com</p>
  <span class="rule rule--green" style="left:354px;top:52px;width:27px;"></span>
  <span class="rule rule--navy" style="left:354px;top:58px;width:27px;"></span>
  <div class="band" style="left:9px;top:476px;width:372px;height:10px;">
    <span class="band__block" style="left:300px;width:22px;"></span>
    <span class="band__block" style="left:345px;width:27px;"></span>
  </div>
</section>

<!-- Envelope -->
<section class="sheet envelope" style="left:414px;top:22px;width:262px;height:226px;">
  <svg class="abs" style="left:0;top:0;" width="262" height="226" aria-hidden="true">
    <path d="M24 10 H240 L248 51 H16 Z" fill="#0f8a4c"/>
    <path d="M18 51 V212 H244 V51" fill="none" stroke="#e6a9b8" stroke-width="0.6"/>
  </svg>
  <div class="panel" style="left:18px;top:51px;width:226px;height:102px;"></div>
  <div class="brand" style="left:186px;top:57px;width:46px;height:36px;">
    <span class="brand__square" style="width:22px;height:22px;"></span>
    <span class="brand__name" style="font-size:7px;">Halvorsk</span>
  </div>
  <div class="brand brand--light" style="left:116px;top:19px;width:30px;height:20px;">
    <span class="brand__square" style="width:10px;height:10px;"></span>
    <span class="brand__name" style="font-size:4px;">Halvorsk</span>
  </div>
  <div class="window" style="left:35px;top:97px;width:96px;height:28px;"></div>
  <span class="rule rule--green" style="left:18px;top:136px;width:14px;height:1.5px;"></span>
  <span class="rule rule--navy" style="left:18px;top:140px;width:14px;height:1.5px;"></span>
  <p class="contact" style="left:34px;top:134px;font-size:3px;">2150 Meridian Park Way Suite 410 Palm Harbor Bay, Florida 34299<br><b>P</b> (941) 555-0142 <b>F</b> (941) 555-0187 <b>E</b> dorian@halvorsklaw.com</p>
  <div class="band" style="left:20px;top:158px;width:224px;height:11px;">
    <p class="abs" style="left:0;width:180px;top:2px;text-align:center;font-size:5px;color:#fff;">www.halvorsklaw.com</p>
    <span class="band__block" style="left:179px;width:14px;"></span>
    <span class="band__block" style="left:207px;width:17px;"></span>
  </div>
</section>

<!-- Presentation folder -->
<section class="sheet folder" style="left:681px;top:22px;width:272px;height:226px;">
  <div class="abs" style="left:12px;top:3px;width:124px;height:147px;background:var(--green);"></div>
  <div class="abs" style="left:136px;top:3px;width:123px;height:147px;background:var(--navy);"></div>
  <div class="brand brand--light" style="left:58px;top:62px;width:34px;height:26px;">
    <span class="brand__square" style="width:14px;height:14px;"></span>
    <span class="brand__name" style="font-size:5px;">Halvorsk</span>
  </div>
  <div class="brand brand--light" style="left:216px;top:11px;width:34px;height:26px;">
    <span class="brand__square" style="width:14px;height:14px;background:var(--green);"></span>
    <span class="brand__name" style="font-size:5px;">Halvorsk</span>
  </div>
  <p class="contact" style="left:12px;top:152px;font-size:2.4px;">2150 Meridian Park Way Suite 410 Palm Harbor Bay, Florida 34299<br>(941) 555-0142 · dorian@halvorsklaw.com</p>
  <p class="contact" style="left:140px;top:153px;font-size:2.4px;">www.halvorsklaw.com</p>
  <div class="band" style="left:12px;top:162px;width:247px;height:5px;">
    <span class="band__block" style="left:222px;width:8px;"></span>
    <span class="band__block" style="left:239px;width:8px;"></span>
  </div>
  <svg class="abs" style="left:0;top:150px;" width="272" height="76" aria-hidden="true">
    <path d="M12 17 V70 H132 L136 62 L140 70 H266 L259 17" fill="none" stroke="#e6a9b8" stroke-width="0.6"/>
    <path d="M136 17 V62" stroke="#e6a9b8" stroke-width="0.6" stroke-dasharray="2 2"/>
    <path d="M180 38 l5 -5 M222 33 l5 5 M180 50 l5 5 M227 50 l-5 5" stroke="#d9d9d9" stroke-width="0.6"/>
  </svg>
</section>

<!-- Business card, front -->
<section class="sheet card-front" style="left:962px;top:56px;width:231px;height:146px;">
  <div class="panel" style="left:8px;top:8px;width:215px;height:132px;"></div>
  <div class="abs" style="left:11px;top:27px;width:90px;height:35px;background:linear-gradient(90deg,#e1e3e6,#f3f4f6);"></div>
  <p class="abs" style="left:39px;top:37px;font-size:8.5px;color:#444;">Dorian Halvorsk, P.A.</p>
  <p class="abs" style="left:39px;top:49px;font-size:5px;color:var(--accent-red);">Attorney at Law</p>
  <div class="brand" style="left:142px;top:29px;width:46px;height:36px;">
    <span class="brand__square" style="width:20px;height:20px;"></span>
    <span class="brand__name" style="font-size:7px;">Halvorsk</span>
  </div>
  <span class="rule rule--green" style="left:13px;top:106px;width:34px;height:3px;"></span>
  <span class="rule rule--navy" style="left:13px;top:116px;width:34px;height:3px;"></span>
  <p class="contact" style="left:50px;top:103px;font-size:5.3px;line-height:1.9;">2150 Meridian Park Way Suite 410 Palm Harbor Bay, Florida 34299<br><b>P</b> (941) 555-0142 <b>F</b> (941) 555-0187 <b>E</b> dorian@halvorsklaw.com</p>
</section>

<!-- Business card, back -->
<section class="sheet card-back" style="left:964px;top:225px;width:229px;height:146px;">
  <div class="abs" style="left:12px;top:11px;width:209px;height:97px;background:var(--green);"></div>
  <div class="brand brand--light" style="left:82px;top:27px;width:64px;height:52px;">
    <span class="brand__square" style="width:32px;height:32px;"></span>
    <span class="brand__name" style="font-size:9px;">Halvorsk</span>
  </div>
  <p class="abs" style="left:12px;width:209px;top:84px;text-align:center;font-size:10.5px;color:#fff;">Personal Injury Attorneys</p>
  <p class="abs" style="left:12px;width:209px;top:108px;text-align:center;font-size:5px;font-weight:600;color:#555;">www.halvorsklaw.com</p>
  <div class="band" style="left:12px;top:119px;width:209px;height:17px;"></div>
</section>

<!-- Compliment slip -->
<section class="sheet compliments" style="left:418px;top:259px;width:537px;height:251px;">
  <div class="panel" style="left:12px;top:11px;width:515px;height:228px;"></div>
  <h1 class="abs" style="left:75px;top:55px;font-size:18px;font-weight:400;color:#222;">WithCompliments</h1>
  <div class="brand" style="left:416px;top:32px;width:84px;height:68px;">
    <span class="brand__square" style="width:42px;height:42px;"></span>
    <span class="brand__name" style="font-size:12px;">Halvorsk</span>
  </div>
  <span class="rule rule--green" style="left:12px;top:205px;width:38px;height:3px;"></span>
  <span class="rule rule--navy" style="left:12px;top:215px;width:38px;height:3px;"></span>
  <p class="contact" style="left:54px;top:201px;font-size:6.5px;line-height:1.65;">2150 Meridian Park Way Suite 410 Palm Harbor Bay, Florida 34299<br><b>P</b> (941) 555-0142 <b>F</b> (941) 555-0187 <b>E</b> dorian@halvorsklaw.com</p>
  <div class="band" style="left:12px;top:225px;width:515px;height:14px;">
    <span class="band__block" style="left:413px;width:30px;"></span>
    <span class="band__block" style="left:475px;width:40px;"></span>
  </div>
</section>

</body>
</html>
```